" Quintela advogados é um escritório de advocacia de grande porte atuando em 6 Estados, sendo em 3 deles temos filial em funcionamento, além da matriz (Curitiba). "

```html
<!DOCTYPE html>
<html lang="pt-BR">
<head>
<meta charset="UTF-8">
<title>Quintela advogados — Papel timbrado</title>
<link href="https://fonts.googleapis.com/css2?family=Cinzel:wght@400&family=Open+Sans:wght@300;400;600;700&display=swap" rel="stylesheet">
<style>
  :root {
    --backdrop: #e9e7e4;
    --paper: #ffffff;
    --ink: #1a1a1a;
    --body-text: #8c8c8c;
    --headline: #9ccbe0;
    --accent-red: #c0392b;
    --rule-grey: #bdbdbd;
    --signature-tone: #9a9a9a;
  }
  * { box-sizing: border-box; margin: 0; padding: 0; }
  html, body {
    width: 1200px; height: 1200px; overflow: hidden;
    background: var(--backdrop);
    font-family: "Open Sans", Arial, sans-serif;
  }
  .letterhead {
    position: absolute; left: 210px; top: 105px;
    width: 780px; height: 990px;
    background: var(--paper);
    box-shadow: 0 6px 24px rgba(0,0,0,0.18);
  }
  .side-mark {
    position: absolute; left: 0; top: 92px;
    width: 18px; height: 126px; background: var(--ink);
  }
  .brand {
    position: absolute; left: 40px; top: 150px;
    display: flex; align-items: center; gap: 12px;
  }
  .brand-dot { width: 14px; height: 14px; background: var(--ink); }
  .brand-name {
    font-family: "Cinzel", "Times New Roman", serif;
    font-weight: 400; font-size: 30px; color: var(--ink);
    letter-spacing: 1px;
  }
  .contacts {
    position: absolute; right: 40px; top: 44px;
    text-align: right; color: var(--ink);
  }
  .contact-line {
    display: flex; justify-content: flex-end; align-items: center;
    gap: 8px; font-size: 15px; line-height: 24px;
  }
  .contact-line.phone { font-size: 17px; }
  .contact-icon { width: 13px; height: 13px; }
  .address { font-size: 10px; line-height: 14px; margin-top: 6px; color: #444; }
  .headline {
    position: absolute; left: 72px; top: 300px;
    font-weight: 300; font-size: 44px; color: var(--headline);
    letter-spacing: 1px;
  }
  .body-copy {
    position: absolute; left: 72px; top: 365px; width: 640px;
    font-size: 13.5px; line-height: 21px; color: var(--body-text);
  }
  .body-copy p { margin-bottom: 21px; }
  .sign-off {
    position: absolute; right: 40px; top: 720px; width: 300px;
    text-align: right;
  }
  .signature {
    display: block; margin-left: auto; width: 150px; height: 50px;
    background: linear-gradient(90deg, rgba(154,154,154,0.15), rgba(154,154,154,0.45));
    border-radius: 25px;
  }
  .signer-role { font-weight: 700; font-size: 14px; color: var(--ink); margin-top: 6px; }
  .signer-note { font-size: 12px; color: var(--accent-red); margin-top: 3px; }
  .signer-site { font-size: 12px; color: var(--body-text); margin-top: 3px; }
  .footer-rule {
    position: absolute; left: 0; right: 0; bottom: 30px;
    height: 3px; background: var(--rule-grey);
  }
  .footer-band {
    position: absolute; left: 0; right: 0; bottom: 0;
    height: 22px; background: var(--ink);
  }
</style>
</head>
<body>
  <main class="letterhead">
    <div class="side-mark"></div>

    <div class="brand">
      <span class="brand-dot"></span>
      <span class="brand-name">Quintela advogados</span>
    </div>

    <div class="contacts">
      <div class="contact-line phone">(41) 3050-2284
        <svg class="contact-icon" viewBox="0 0 10 10"><circle cx="5" cy="5" r="5" fill="#1a1a1a"/><path d="M3.3 2.6 L4.2 3.5 L3.8 4.1 Q4.6 5.6 5.9 6.2 L6.5 5.8 L7.4 6.7 L6.8 7.4 Q4.3 7 2.6 3.2 Z" fill="#fff"/></svg>
      </div>
      <div class="contact-line">contato@quintelaadv.com.br
        <svg class="contact-icon" viewBox="0 0 10 10"><circle cx="5" cy="5" r="5" fill="#1a1a1a"/><rect x="2.5" y="3.3" width="5" height="3.4" fill="none" stroke="#fff" stroke-width="0.7"/><path d="M2.5 3.3 L5 5.2 L7.5 3.3" fill="none" stroke="#fff" stroke-width="0.7"/></svg>
      </div>
      <div class="contact-line">www.quintelaadv.com.br
        <svg class="contact-icon" viewBox="0 0 10 10"><circle cx="5" cy="5" r="5" fill="#1a1a1a"/><circle cx="5" cy="5" r="2.6" fill="none" stroke="#fff" stroke-width="0.6"/><path d="M2.4 5 H7.6 M5 2.4 V7.6" stroke="#fff" stroke-width="0.6"/></svg>
      </div>
      <div class="address">Rua 9, nº 210 - Centro - Curitiba - PR<br>Cep 80.010-000</div>
    </div>

    <h1 class="headline">HEADLINE</h1>

    <section class="body-copy">
      <p>Lorem ipsum dolor sit amet, consectetur adipiscing elit. Fusce dignissim pretium consectetur. Curabitur tempor posuere massa in varius. Pellentesque viverra nibh eu vehicula mattis. Nullam porta facilisis justo, a feugiat dolor sodales sed. Vestibulum neque nisi, elementum tincidunt metus sit amet, egestas bibendum enim. Aenean a blandit elit, vel rutrum mi. Nunc dapibus turpis sed massa aliquet tincidunt.</p>
      <p>Pellentesque id neque ligula. Nullam posuere, ligula a mattis posuere, lacus nisl adipiscing nunc, eu congue justo est ut diam. Nam quam nibh, dignissim non consequat in, semper eget purus. Nulla eros sapien, viverra vitae metus tempor, congue ornare diam.</p>
      <p>Pellentesque vel nibh tempus, ullamcorper tortor sed, bibendum augue. Phasellus sollicitudin justo et quam aliquam sollicitudin. Sed eget nibh mollis, mattis sem et, viverra nulla.</p>
    </section>

    <div class="sign-off">
      <span class="signature" role="img" aria-label="Handwritten signature"></span>
      <div class="signer-role">Creative Art Director</div>
      <div class="signer-note">Pellentesque id neque ligula. Nulla</div>
      <div class="signer-site">www.estudiolinha.com</div>
    </div>

    <div class="footer-rule"></div>
    <div class="footer-band"></div>
  </main>
</body>
</html>
```